The Tidy Lantern Business Card

I need a business card designed for The Tidy Lantern. The company provides on site support and education to end consumers in the ins and outs of all our digital devices. We advise on product purchase, installation, maintenance and troubleshooting. Anything from cordless phones to home networks.
My initial concept is double sided with the white logo on green on one side and contact details and a small logo on the flip side (logo package attached)
Contact Details:
Miles Fenwright
Managing Director
PO Box 43
Brackton, NSW 2187
Phone: 0438 907 516
email: miles@tidylantern.com.au
web: www.tidylantern.com.au
Target Market(s)
Busy professionals and retired folks.
Industry/Entity Type
Education
Look and feel

```html
<!DOCTYPE html>
<html lang="en">
<head>
<meta charset="utf-8">
<title>The Tidy Lantern – Business Card</title>
<link href="https://fonts.googleapis.com/css2?family=Questrial&family=Montserrat:wght@400;600&display=swap" rel="stylesheet">
<style>
  :root {
    --backdrop: #ecebe6;
    --leaf-green: #7cb53d;
    --card-white: #ffffff;
    --ink-navy: #1d2a3a;
    --line-white: rgba(255,255,255,0.85);
    --shadow: rgba(0,0,0,0.18);
  }
  * { margin: 0; padding: 0; box-sizing: border-box; }
  html, body {
    width: 1200px; height: 784px; overflow: hidden;
    background: var(--backdrop);
  }
  .sheet {
    width: 1200px; height: 784px;
    display: flex; align-items: center; justify-content: center; gap: 40px;
  }
  .card {
    width: 560px; height: 320px;
    box-shadow: 0 6px 18px var(--shadow);
    position: relative; overflow: hidden;
  }
  .card--contact { background: var(--leaf-green); color: var(--card-white); }
  .card--brand { background: var(--card-white); }

  .contact-brand {
    position: absolute; left: 34px; top: 150px; width: 150px;
    display: flex; flex-direction: column; align-items: center; gap: 12px;
  }
  .brand-dot {
    width: 34px; height: 34px; border-radius: 50%;
    background: var(--card-white);
  }
  .brand-name {
    font-family: "Questrial", sans-serif;
    font-size: 24px; line-height: 1.05; text-align: center;
    letter-spacing: 0.5px;
  }
  .divider {
    position: absolute; left: 206px; top: 128px;
    width: 1px; height: 140px; background: var(--line-white);
  }
  .details {
    position: absolute; left: 222px; top: 128px;
    font-family: "Montserrat", sans-serif;
  }
  .person-name { font-size: 15px; font-weight: 600; }
  .person-title { font-size: 10.5px; margin-bottom: 12px; }
  .detail-row {
    display: flex; align-items: center; gap: 6px;
    font-size: 12px; line-height: 19px;
  }
  .detail-row svg { width: 12px; height: 12px; fill: var(--card-white); flex: none; }

  .brand-lockup {
    position: absolute; inset: 0;
    display: flex; flex-direction: column; align-items: center; justify-content: center; gap: 18px;
  }
  .brand-lockup .brand-dot { width: 46px; height: 46px; background: var(--leaf-green); }
  .brand-lockup .brand-name {
    color: var(--ink-navy); font-size: 40px;
  }
</style>
</head>
<body>
<main class="sheet">
  <section class="card card--contact">
    <div class="contact-brand">
      <span class="brand-dot"></span>
      <p class="brand-name">The Tidy<br>Lantern</p>
    </div>
    <span class="divider"></span>
    <div class="details">
      <p class="person-name">Miles Fenwright</p>
      <p class="person-title">Managing Director</p>
      <p class="detail-row">
        <svg viewBox="0 0 24 24" aria-hidden="true"><path d="M6.6 10.8a15.1 15.1 0 0 0 6.6 6.6l2.2-2.2a1 1 0 0 1 1-.25 11.4 11.4 0 0 0 3.6.57 1 1 0 0 1 1 1V20a1 1 0 0 1-1 1A17 17 0 0 1 3 4a1 1 0 0 1 1-1h3.5a1 1 0 0 1 1 1c0 1.25.2 2.45.57 3.57a1 1 0 0 1-.25 1z"/></svg>
        0438 907 516
      </p>
      <p class="detail-row">
        <svg viewBox="0 0 24 24" aria-hidden="true"><path d="M2 5h20v14H2z M3.5 6.5 12 13l8.5-6.5" fill="none" stroke="#fff" stroke-width="2"/></svg>
        miles@tidylantern.com.au
      </p>
      <p class="detail-row">
        <svg viewBox="0 0 24 24" aria-hidden="true"><g fill="none" stroke="#fff" stroke-width="2"><circle cx="12" cy="12" r="9"/><ellipse cx="12" cy="12" rx="4" ry="9"/><path d="M3 12h18"/></g></svg>
        www.tidylantern.com.au
      </p>
      <p class="detail-row">
        <svg viewBox="0 0 24 24" aria-hidden="true"><path d="M12 3 2 12h3v9h5v-6h4v6h5v-9h3z"/></svg>
        PO Box 43, Brackton, NSW 2187
      </p>
    </div>
  </section>

  <section class="card card--brand">
    <div class="brand-lockup">
      <span class="brand-dot"></span>
      <p class="brand-name">The Tidy Lantern</p>
    </div>
  </section>
</main>
</body>
</html>
```